Gas utility and appliance store needs awesome web design

The Flint Hearth is a South African based brick and mortar shop looking to improve it's on-line presence.
We cover the whole gambit or products, appliances, information, services, installations and utility related to domestic gas (in SA still considered an alternative fuel) with our most important offerings being the sale of the gas (LPG) itself in combination with high end kitchen and household gas based appliances (stoves, cookers, heaters, fireplaces etc)
Wesite needs to portray our professional (been in the market since 47), family owned (3'rd gen now) roots - it should create the impression of a market leader - and must also portray our domestic (read man in the street) focus and practical approach.
Something professional but light-hearted enough for the general public.
Design must reinforce the belief that LPG is a green,safe and affordable fuel option for domestic use

Target Market(s)

upper middle class market 25-70

Industry/Entity Type

Appliance

Requirements
Must have
• landing page
our company
sustainability
contact us page
menu bar with links to pages (shop, specific information etc)

```html
<!DOCTYPE html>
<html lang="en">
<head>
<meta charset="utf-8">
<title>The Flint Hearth — We Make Gas Hot</title>
<link rel="stylesheet" href="https://fonts.googleapis.com/css2?family=Ubuntu:wght@400;500;700&family=Arimo:wght@400;700&family=Quicksand:wght@300;400&display=swap">
<style>
:root{
  --blue:#0d5a8f;
  --blue-deep:#0a4a78;
  --blue-bright:#1a86c8;
  --orange:#ee7d22;
  --orange-light:#f59a2e;
  --orange-dark:#c9581a;
  --grey-text:#555;
  --grey-line:#d6d6d6;
  --panel:#f5f5f5;
  --white:#fff;
  --ink:#2a1a0f;
}
*{margin:0;padding:0;box-sizing:border-box}
html,body{width:1175px;height:1200px;overflow:hidden;background:var(--blue)}
.site{position:absolute;left:0;top:0;width:1150px;height:1174px;transform:scale(1.0217);transform-origin:0 0;font-family:Arimo,Arial,sans-serif;color:var(--grey-text)}
.abs{position:absolute}
.top-band{left:0;top:0;width:1150px;height:87px;background:linear-gradient(var(--blue-deep),var(--blue))}
.hero-band{left:0;top:87px;width:1150px;height:461px;background:linear-gradient(90deg,#d4d8dc,#f7f7f7 20%,#fafafa 80%,#e2e4e6)}
.header{left:92px;top:0;width:965px;height:125px;background:linear-gradient(#fff,#ececec);border-radius:0 0 10px 10px;box-shadow:0 2px 4px rgba(0,0,0,.3)}
.brand{left:140px;top:44px;display:flex;align-items:center;gap:8px;font-family:Ubuntu,sans-serif;font-weight:700;font-size:19px;color:var(--blue-bright);width:130px;line-height:1.1}
.brand-dot{width:16px;height:16px;border-radius:50%;background:var(--orange);flex:none}
.tagline{left:274px;top:58px;font-family:Quicksand,sans-serif;font-weight:300;font-size:26px;letter-spacing:6px;line-height:29px;color:#777}
.follow{left:700px;top:67px;width:357px;height:31px;background:linear-gradient(90deg,rgba(220,220,220,0),#ddd 30%);display:flex;align-items:center;gap:8px;padding-left:12px;font-size:14px;color:#666}
.follow-label{font-family:Ubuntu,sans-serif;font-weight:700;font-size:19px;color:var(--orange);margin-right:6px}
.social{display:flex;align-items:center;gap:5px;margin-right:8px}
.social i{width:22px;height:22px;border-radius:3px;background:var(--blue-bright);display:block}
.slider{left:93px;top:137px;width:963px;height:401px;border-radius:12px;background:repeating-linear-gradient(45deg,#e9e9e9 0 2px,#f6f6f6 2px 4px);box-shadow:0 0 3px rgba(0,0,0,.3)}
.slide{left:108px;top:150px;width:935px;height:371px;border-radius:8px;background:linear-gradient(90deg,#5a3a22 0%,#c0702e 25%,#7a4a2c 45%,#8aa8cc 65%,#cfe0f0 80%,#4c5e72 100%)}
.arrow{width:52px;height:80px;top:282px;background:#eee;border-radius:40px;box-shadow:0 0 3px rgba(0,0,0,.3)}
.arrow svg{position:absolute;left:7px;top:21px}
.nav{left:0;top:548px;width:1150px;height:42px;background:linear-gradient(var(--orange-light),var(--orange) 60%,var(--orange-dark));font-family:Ubuntu,sans-serif;font-weight:500;font-size:14px;color:#fff}
.nav-item{position:absolute;top:0;height:42px;line-height:42px;transform:translateX(-50%)}
.nav-home{left:97px;top:7px;width:83px;height:29px;border-radius:8px;background:linear-gradient(#2a7fc0,var(--blue-deep));text-align:center;line-height:29px;box-shadow:0 1px 2px rgba(0,0,0,.4)}
.nav-div{position:absolute;top:4px;width:1px;height:34px;background:rgba(255,255,255,.35)}
.search{left:856px;top:9px;width:190px;height:25px;border-radius:13px;background:var(--orange-dark);font-family:Arimo,sans-serif;font-weight:400;font-size:13px;padding:6px 11px;color:#fff}
.search-btn{left:1034px;top:556px;width:27px;height:27px;border-radius:50%;background:radial-gradient(circle at 40% 35%,#6ec4f4,var(--blue-bright))}
.main{left:77px;top:590px;width:996px;height:584px;background:#fff}
.about{left:90px;top:610px;width:645px;height:267px;border:1px solid #ddd;border-radius:8px;background:linear-gradient(#fff,var(--panel))}
.about-head{left:0;top:0;width:643px;height:41px;border-radius:8px 8px 0 0;background:linear-gradient(#2a7fc0,var(--blue-deep));font-family:Ubuntu,sans-serif;font-weight:700;font-size:20px;color:#fff;padding:8px 0 0 54px}
.about-head svg{position:absolute;left:12px;top:4px}
.about-text{left:13px;top:64px;width:329px;font-size:12.5px;line-height:20px;text-align:justify}
.about-text p+p{margin-top:11px}
.about-photo{left:363px;top:58px;width:268px;height:183px;border-radius:8px;background:linear-gradient(160deg,#8a9098,#6a6e70 40%,#5c4a3c 75%,#3e3a36)}
.btn-orange{left:13px;top:227px;width:84px;height:24px;border-radius:5px;background:linear-gradient(#f6b21a,#e48a0c);font-weight:700;font-size:12.5px;color:#fff;text-align:center;line-height:24px}
.news-title{left:825px;top:620px;font-family:Ubuntu,sans-serif;font-weight:700;font-size:20px;color:#555}
.news-title span{color:var(--orange)}
.news-icon{left:778px;top:612px}
.news-item{left:773px;width:277px;height:60px}
.news-badge{left:0;top:0;width:40px;height:40px;border-radius:50%;background:var(--blue);border:2px dotted #7ab6de;color:#fff;font-weight:700;font-size:11px;text-align:center;line-height:14px;padding-top:4px}
.news-body{left:51px;top:-1px;font-size:11px;line-height:18px;color:#555;letter-spacing:.2px}
.news-body b{color:var(--blue-bright);font-size:11.5px}
.news-sep{left:776px;width:274px;border-top:1px dotted #888}
.more{left:981px;top:880px;font-weight:700;font-size:12px;color:var(--blue-bright)}
.services{left:91px;top:924px;width:968px;height:163px;border:1px solid #ddd;background:#fafafa}
.card{top:915px;width:212px;height:159px;border-radius:0 0 8px 8px;background:linear-gradient(var(--orange-light),var(--orange));color:#fff}
.card::before{content:"";position:absolute;left:-8px;top:0;width:228px;height:8px;background:#b55a14;border-radius:4px 4px 0 0;z-index:-1}
.card h3{position:absolute;left:16px;top:13px;font-family:Ubuntu,sans-serif;font-weight:700;font-size:17.5px}
.card svg{position:absolute;left:4px;top:50px}
.card p{position:absolute;left:78px;top:52px;width:123px;font-size:12px;line-height:16px;text-align:justify}
.card .pill{position:absolute;right:10px;top:129px;height:22px;padding:0 7px;border-radius:11px;background:#fff;color:var(--orange);font-size:12px;line-height:22px}
.footer{left:79px;top:1113px;width:994px;height:61px;background:#dedede;text-align:center;font-size:12px;color:#666}
.footer nav{padding-top:13px;word-spacing:2px}
.footer nav span{margin:0 9px}
.footer p{margin-top:9px}
</style>
</head>
<body>
<div class="site">
  <div class="abs top-band"></div>
  <div class="abs hero-band"></div>

  <header class="abs header"></header>
  <div class="abs brand"><i class="brand-dot"></i>The Flint Hearth</div>
  <div class="abs tagline">WE MAKE<br>GAS HOT</div>
  <div class="abs follow">
    <span class="follow-label">Follow us on:</span>
    <span class="social"><i></i>Linkbook</span>
    <span class="social"><i></i>Chirper</span>
  </div>

  <div class="abs slider"></div>
  <div class="abs slide" role="img" aria-label="Gas refinery lit at night beside an oil pump jack under a bright sky"></div>
  <div class="abs arrow" style="left:76px">
    <svg width="38" height="38" viewBox="0 0 38 38"><circle cx="19" cy="19" r="18" fill="#ccc" stroke="#999"/><path d="M10 19l9-8v5h9v6h-9v5z" fill="#666"/></svg>
  </div>
  <div class="abs arrow" style="left:1022px">
    <svg width="38" height="38" viewBox="0 0 38 38"><circle cx="19" cy="19" r="18" fill="#ccc" stroke="#999"/><path d="M28 19l-9-8v5h-9v6h9v5z" fill="#666"/></svg>
  </div>

  <nav class="abs nav">
    <div class="abs nav-home">HOME</div>
    <i class="nav-div" style="left:195px"></i>
    <span class="nav-item" style="left:243px">ABOUT</span>
    <i class="nav-div" style="left:299px"></i>
    <span class="nav-item" style="left:358px">SHOP</span>
    <i class="nav-div" style="left:430px"></i>
    <span class="nav-item" style="left:537px">SPECIFIC INFORMATION</span>
    <i class="nav-div" style="left:647px"></i>
    <span class="nav-item" style="left:708px">CONTACT US</span>
    <div class="abs search">Type here to search...</div>
  </nav>
  <div class="abs search-btn"></div>

  <main class="abs main"></main>

  <section class="abs about">
    <h2 class="abs about-head">
      <svg width="34" height="34" viewBox="0 0 34 34"><text x="2" y="30" font-family="Ubuntu" font-weight="700" font-size="26" fill="#f3b11b">?</text><rect x="18" y="6" width="9" height="24" rx="3" fill="#fff"/><circle cx="22.5" cy="5" r="3.5" fill="#fff"/></svg>
      Who we Are
    </h2>
    <div class="abs about-text">
      <p>Lorem Ipsum is simply dummy text of the printing and type-setting industry. Lorem Ipsum has been the industry's standard dummy text ever since the 1500s, when an unknown printer took a galley of type</p>
      <p>Lorem Ipsum has been the industry's standard dummy text ever since the 1500s, when an unknown printer took a galley of type</p>
    </div>
    <div class="abs about-photo" role="img" aria-label="Gas workers in hard hats tending valves and pipework at a plant"></div>
    <div class="abs btn-orange">Read more</div>
  </section>

  <svg class="abs news-icon" width="36" height="36" viewBox="0 0 36 36"><rect x="6" y="2" width="24" height="26" rx="2" fill="#f08a1c"/><path d="M11 22a2 2 0 1 0 0.1 0M11 16a7 7 0 0 1 7 7M11 10a13 13 0 0 1 13 13" stroke="#fff" stroke-width="2.5" fill="none"/><ellipse cx="18" cy="31" rx="13" ry="3" fill="#ccc"/></svg>
  <h2 class="abs news-title"><span>News &amp;</span> Updates</h2>

  <div class="abs news-item" style="top:669px">
    <div class="abs news-badge">April<br>20</div>
    <div class="abs news-body"><b>lorum ipsum: PaperLane is simply</b><br>from Around the Web Favorite Links from<br>Around the Web April 2nd-6th</div>
  </div>
  <div class="abs news-sep" style="top:729px"></div>
  <div class="abs news-item" style="top:743px">
    <div class="abs news-badge">April<br>20</div>
    <div class="abs news-body"><b>lorum ipsum: PaperLane is simply</b><br>from Around the Web Favorite Links from<br>Around the Web April 2nd-6th</div>
  </div>
  <div class="abs news-sep" style="top:803px"></div>
  <div class="abs news-item" style="top:820px">
    <div class="abs news-badge">April<br>20</div>
    <div class="abs news-body"><b>lorum ipsum: PaperLane is simply</b><br>from Around the Web Favorite Links from<br>Around the Web April 2nd-6th</div>
  </div>
  <div class="abs more">Moreinfo[+]</div>

  <div class="abs services"></div>

  <article class="abs card" style="left:104px">
    <h3>For My Home</h3>
    <svg width="70" height="64" viewBox="0 0 70 64"><path d="M4 32L35 4l31 28-5 4-26-23L9 36z" fill="var(--ink)"/><path d="M14 34L35 15l21 19v28H41V44H29v18H14z" fill="var(--ink)"/></svg>
    <p>Lorem Ipsum is simply dummy text of the printing and typeset-ting industry.</p>
    <span class="pill">Read more</span>
  </article>
  <article class="abs card" style="left:345px">
    <h3>For My Business</h3>
    <svg width="70" height="64" viewBox="0 0 70 64"><rect x="10" y="20" width="50" height="38" rx="5" fill="var(--ink)"/><path d="M26 20v-8h18v8" stroke="var(--ink)" stroke-width="5" fill="none"/><rect x="10" y="34" width="50" height="3" fill="#f0892a"/></svg>
    <p>Lorem Ipsum is simply dummy text of the printing and typeset-ting industry.</p>
    <span class="pill">Read more</span>
  </article>
  <article class="abs card" style="left:590px">
    <h3>Energy Efficiency</h3>
    <svg width="70" height="72" viewBox="0 0 70 72"><path d="M38 4L16 40h15L22 70l30-42H37z" fill="var(--ink)"/></svg>
    <p>Lorem Ipsum is simply dummy text of the printing and typeset-ting industry.</p>
    <span class="pill">Read more</span>
  </article>
  <article class="abs card" style="left:835px">
    <h3>Natural Gas Safety</h3>
    <svg width="70" height="64" viewBox="0 0 70 64"><rect x="12" y="6" width="30" height="54" rx="4" fill="var(--ink)"/><rect x="18" y="12" width="18" height="14" rx="2" fill="#f0892a"/><path d="M42 16l10 8v26a4 4 0 0 0 8 0V22" stroke="var(--ink)" stroke-width="4" fill="none"/></svg>
    <p>Lorem Ipsum is simply dummy text of the printing and typeset-ting industry.</p>
    <span class="pill">Read more</span>
  </article>

  <footer class="abs footer">
    <nav>Home<span>|</span>About<span>|</span>Shop<span>|</span>Specific Information<span>|</span>Contact us</nav>
    <p>Copyright © 2012 The Flint Hearth. All Right Reserved</p>
  </footer>
</div>
</body>
</html>
```